KT Appraisals BV business cards (a financial services company)

I am looking for a business card design that stands out in the financial advisory field of business & intellectual property valuation. The business card design should be conservative, yet different. Address details have changed since the attached business card. New address is:

Dorpelstraat 27
4817 KM Leiden
The Netherlands

Telephone number remains the same.

```html
<!DOCTYPE html>
<html lang="en">
<head>
<meta charset="utf-8">
<title>KT Appraisals BV – Business Cards</title>
<link rel="stylesheet" href="https://fonts.googleapis.com/css2?family=Nunito+Sans:wght@300;400;600&display=swap">
<style>
  :root {
    --stage: #1d1d1f;
    --card-dark: #2a2a2c;
    --card-light: #ffffff;
    --silver: #a9a9ab;
    --ink: #3a3a3c;
    --ink-soft: #8a8a8c;
  }
  * { box-sizing: border-box; margin: 0; padding: 0; }
  html, body {
    width: 1200px; height: 800px; overflow: hidden;
    background: var(--stage);
    font-family: "Nunito Sans", sans-serif;
  }
  .canvas {
    width: 1200px; height: 800px;
    display: flex; align-items: center; justify-content: center; gap: 48px;
  }
  .card {
    width: 525px; height: 300px;
    position: relative;
    box-shadow: 0 18px 40px rgba(0,0,0,.45);
  }
  .card--front {
    background: var(--card-dark);
    display: flex; align-items: center; justify-content: center;
  }
  .brand {
    display: flex; align-items: center; gap: 14px;
    color: var(--silver);
  }
  .brand__square {
    width: 22px; height: 22px;
    background: var(--silver);
  }
  .brand__name {
    font-weight: 300;
    font-size: 30px;
    letter-spacing: 3px;
    text-transform: uppercase;
  }
  .card--back {
    background: var(--card-light);
    color: var(--ink);
  }
  .details {
    position: absolute;
    right: 56px; top: 40px;
    text-align: right;
    font-size: 13px; line-height: 1.4;
  }
  .details__name {
    font-size: 17px; font-weight: 300;
    letter-spacing: 1px; color: var(--ink-soft);
  }
  .details__role { font-size: 13px; margin-bottom: 14px; }
  .details__contact { margin-bottom: 14px; }
  .details__label { font-weight: 600; }
  .details__web { font-weight: 600; }
  .details__address { color: var(--ink-soft); }
  .tagline {
    position: absolute;
    right: 56px; bottom: 30px;
    font-size: 12px; letter-spacing: .6px;
    text-transform: uppercase; color: var(--ink);
  }
</style>
</head>
<body>
<main class="canvas">
  <section class="card card--front" aria-label="Card front">
    <div class="brand">
      <span class="brand__square"></span>
      <span class="brand__name">KT Appraisals</span>
    </div>
  </section>

  <section class="card card--back" aria-label="Card back">
    <div class="details">
      <p class="details__name">MARTIN HALE, CFA, ASA, RV</p>
      <p class="details__role">Managing Director</p>
      <p class="details__contact">
        <span class="details__label">t:</span>+31 (0)71 384 2619<br>
        <span class="details__label">e:</span>mhale@ktappraisals.com<br>
        <span>www.</span><span class="details__web">ktappraisals</span><span>.com</span>
      </p>
      <p class="details__address">
        Dorpelstraat 27, 4817 KM Leiden<br>
        The Netherlands
      </p>
    </div>
    <p class="tagline">Business and Intellectual Property Valuations</p>
  </section>
</main>
</body>
</html>
```